Redesign logo + Business card for Car tuning/diagnostics

Hi, after a LOGO AND BUSINESS CARD. I need a double-sided business card to be designed. And information added to it as below. I have added some pictures as a sample of type of cards I like…

Update: i have seen some enteries and i think it would look better if there is a big logo on one side and it has services under the big logo. And on the other side we can have contact details. However if you have different ideas I am open to suggestions

Will need high quality and editable files to print.

Name: Rashid
Mobile/WhatsApp: 07700900461
Email: Zed@brantlytune.com
Space to add snapchat and Instagram account if I decide to create one later.

Services to include in list ECU Remapping, Mileage correction, DPF issues, Retrofitting, Programming and Coding, Diagnostic Scans, Spare keys, Engine carbon Cleaning

```html
<!DOCTYPE html>
<html lang="en">
<head>
<meta charset="utf-8">
<title>Brantly Tuning – Business Card</title>
<link rel="stylesheet" href="https://fonts.googleapis.com/css2?family=Montserrat:wght@600;700;800&display=swap">
<style>
  :root {
    --page: #ffffff;
    --black: #050505;
    --deep-red: #5a1210;
    --red: #d23a2f;
    --white: #ffffff;
    --shadow: rgba(0,0,0,0.35);
  }
  * { margin: 0; padding: 0; box-sizing: border-box; }
  html, body {
    width: 999px; height: 1200px; overflow: hidden;
    background: var(--page);
    font-family: "Montserrat", Arial, sans-serif;
    color: var(--white);
  }
  .card {
    position: absolute; left: 50px; width: 853px; height: 483px;
    border-radius: 28px; overflow: hidden;
    box-shadow: 14px 16px 24px var(--shadow);
  }
  .card--front {
    top: 50px;
    background: linear-gradient(to bottom, var(--black) 0%, var(--black) 55%, var(--deep-red) 75%, var(--red) 100%);
  }
  .card--back {
    top: 622px;
    background: linear-gradient(to bottom, var(--red) 0%, var(--deep-red) 25%, var(--black) 44%, var(--black) 100%);
  }
  .wordmark {
    position: absolute; font-weight: 800; letter-spacing: 3px;
    white-space: nowrap; line-height: 1;
  }
  .card--front .wordmark { left: 0; right: 0; text-align: center; top: 228px; font-size: 58px; }
  .card--back .wordmark { left: 56px; top: 236px; font-size: 38px; }
  .services {
    position: absolute; left: 0; right: 0; top: 406px;
    text-align: center; font-weight: 600; font-size: 16.5px; line-height: 25px;
  }
  .holder-name {
    position: absolute; left: 563px; width: 270px; text-align: center; top: 98px;
    font-size: 40px; font-weight: 700; text-decoration: underline;
    text-decoration-thickness: 3px; text-underline-offset: 5px;
  }
  .contacts { position: absolute; left: 494px; top: 220px; list-style: none; }
  .contact {
    display: flex; align-items: center; height: 44px; margin-bottom: 14.5px;
    font-weight: 700; font-size: 17.5px;
  }
  .contact__icon {
    width: 44px; height: 44px; border-radius: 50%; background: var(--red);
    display: flex; align-items: center; justify-content: center; margin-right: 12px; flex: none;
  }
</style>
</head>
<body>
  <section class="card card--front">
    <div class="wordmark">BRANTLY TUNING</div>
    <p class="services">
      ECU Remapping - Mileage correction - DPF issues - Retrofitting<br>
      Programming and Coding - Diagnostic Scans - Spare keys - Engine carbon Cleaning
    </p>
  </section>

  <section class="card card--back">
    <h1 class="holder-name">Rashid</h1>
    <div class="wordmark">BRANTLY TUNING</div>
    <ul class="contacts">
      <li class="contact">
        <span class="contact__icon">
          <svg width="22" height="22" viewBox="0 0 24 24" aria-hidden="true">
            <path fill="#fff" d="M6.6 10.8a15.1 15.1 0 0 0 6.6 6.6l2.2-2.2c.3-.3.7-.4 1-.2 1.1.4 2.3.6 3.6.6.6 0 1 .4 1 1V20c0 .6-.4 1-1 1A17 17 0 0 1 3 4c0-.6.4-1 1-1h3.5c.6 0 1 .4 1 1 0 1.3.2 2.5.6 3.6.1.3 0 .7-.2 1z"/>
          </svg>
        </span>07700900461
      </li>
      <li class="contact">
        <span class="contact__icon">
          <svg width="22" height="22" viewBox="0 0 24 24" aria-hidden="true">
            <rect x="2" y="5" width="20" height="14" rx="1.5" fill="#fff"/>
            <path d="M3 6.5l9 6.5 9-6.5" fill="none" stroke="#d23a2f" stroke-width="2"/>
          </svg>
        </span>Zed@brantlytune.com
      </li>
      <li class="contact">
        <span class="contact__icon"></span>@brantlytuning
      </li>
      <li class="contact">
        <span class="contact__icon"></span>@brantly.tuningofficial
      </li>
    </ul>
  </section>
</body>
</html>
```